Teodor Ravik, MD Print Package_Trifold

Need a trifold brochure designed. The business is a cosmetic surgery office with cosmetic procedures involving face surgery, body surgery, breast surgery, and skin care treatments. At this point, we would like to see a brochure with some more white space.

A little bit about the doctor for character reference:
Dr. Teodor Ravik believes the art of cosmetic surgery is in listening to his patients. He builds each treatment plan on a solid foundation of communication between doctor and patient and spends a considerable amount of time getting to know the people he treats — taking their goals into account and offering the best options to meet those goals. At our state-of-the-art Bayfield Aesthetic Institute, you are not just a patient; You are our guest.

Their website for further information and for color scheme reference, as the client would like the brochure to match his website (ie: ocean blue/teal, grays and black), is http://www.drtravensolo.example/

Attached is a brochure that the client created a few months back. This shows a general idea of how he would like the layout to be and the information to put on the trifold.

Also Attached are two additional Before & Afters for the brochure, per the client's request. As well as a picture of the Vexa Beam machine that performs these procedures.

Also attached is a brochure intake document for further guidelines as well.
Updates

Industry/Entity Type

Business

Requirements
Must have
• If utilizing any staff photos - please be sure to use Dr. Teodor Ravik, you can find him here:
• http://www.drtravensolo.example/about

```html
<!DOCTYPE html>
<html lang="en">
<head>
<meta charset="utf-8">
<title>Teodor Ravik, MD – Skin Treatments Panel</title>
<link rel="stylesheet" href="https://fonts.googleapis.com/css2?family=Open+Sans:wght@400;700&display=swap">
<style>
  :root {
    --page-bg: #3a3330;
    --sheet-gray: #b7bfbe;
    --sheet-white: #ffffff;
    --wave-teal: #3f7f96;
    --wave-edge: #2f6379;
    --heading-blue: #2a66b8;
    --body-ink: #2b2b2b;
    --skin-deep: #8a5a3e;
    --skin-light: #e9c3b5;
    --skin-pale: #efd6cf;
    --scar-red: #c88a86;
    --rosy: #e4a8a4;
    --frame-white: #ffffff;
  }
  * { margin: 0; padding: 0; box-sizing: border-box; }
  html, body { width: 1200px; height: 900px; overflow: hidden; background: var(--page-bg); }
  .brochure-panel {
    position: absolute; left: 52px; top: 15px; width: 1105px; height: 860px;
    background: var(--sheet-gray); overflow: hidden;
    font-family: "Open Sans", Arial, sans-serif;
  }
  .content-sheet {
    position: absolute; left: 26px; top: 60px; width: 1055px; height: 800px;
    background: linear-gradient(180deg, var(--sheet-white) 0%, var(--sheet-white) 45%, #e4e8e8 75%, #c9cfcf 100%);
  }
  .wave-band { position: absolute; left: 0; top: 0; width: 1105px; height: 200px; }
  .treatment { position: absolute; }
  .treatment h2 {
    font-size: 13.5px; font-weight: 700; color: var(--heading-blue);
    letter-spacing: 0.2px; margin-bottom: 10px;
  }
  .treatment p {
    font-size: 12px; line-height: 16.2px; color: var(--body-ink);
    text-align: justify; position: absolute; left: 0;
  }
  .photo { position: absolute; border-radius: 4px; }
  .photo.rounded-end { border-radius: 4px 4px 18px 4px; }
  .photo.framed { border: 4px solid var(--frame-white); border-radius: 0; }
</style>
</head>
<body>
<main class="brochure-panel">
  <svg class="wave-band" viewBox="0 0 1105 200" aria-hidden="true">
    <path d="M0 190 L0 125 C140 95 300 25 480 25 C650 25 820 70 1105 60 L1105 200 Z" fill="var(--sheet-white)"/>
    <path d="M0 145 C160 110 320 22 490 22 C680 22 850 75 1105 62 L1105 100 C860 118 670 58 490 60 C330 62 160 130 0 158 Z" fill="var(--wave-teal)"/>
    <path d="M0 158 C160 130 330 62 490 60 C670 58 860 118 1105 100" fill="none" stroke="var(--wave-edge)" stroke-width="2"/>
  </svg>

  <section class="content-sheet" style="top:160px;height:700px;background:linear-gradient(180deg,var(--sheet-white) 0%,var(--sheet-white) 30%,#e4e8e8 65%,#c9cfcf 100%);"></section>

  <!-- Row one -->
  <article class="treatment" style="left:71px;top:165px;width:280px;">
    <h2>LASER HAIR REMOVAL</h2>
    <div class="photo" role="img" aria-label="Before and after of laser hair removal on the upper lip" style="left:-5px;top:27px;width:130px;height:136px;background:linear-gradient(135deg,#5a3a28,var(--skin-deep));"></div>
    <div class="photo rounded-end" role="img" aria-label="After laser hair removal, smooth upper lip" style="left:128px;top:27px;width:139px;height:136px;background:linear-gradient(135deg,#9a6a4a,#6e4630);"></div>
    <p style="top:182px;width:277px;">Are you tired of shaving, waxing, tweezing, and plucking? Laser hair removal provides a fast, easy solution for permanent hair reduction, allowing you to look and feel your best without all the hassle. Popular areas for treatment are the lower face, upper lip, underarms, chest, back, bikini and legs. Fees are based on area.</p>
  </article>

  <article class="treatment" style="left:414px;top:165px;width:280px;">
    <h2>SURGICAL &amp; ACNE SCARS</h2>
    <div class="photo" role="img" aria-label="Before scar treatment, raised red scar on skin" style="left:0;top:27px;width:132px;height:111px;background:linear-gradient(160deg,var(--skin-light),var(--scar-red) 50%,var(--skin-light));"></div>
    <div class="photo rounded-end" role="img" aria-label="After scar treatment, faded scar" style="left:136px;top:27px;width:135px;height:111px;background:linear-gradient(160deg,#e6c9c0,#dcb4aa);"></div>
    <p style="top:160px;width:277px;">Imagine yourself with beautiful skin that’s free of scars. No more cover-up, extra clothing, or added daily expenses. With laser treatment for scar removal, unwanted scars can be a thing of the past. Laser scar removal is a non-invasive, advanced approach to scar treatment that offers excellent results without the discomfort and downtime of surgery.</p>
  </article>

  <article class="treatment" style="left:767px;top:165px;width:280px;">
    <h2>R0SACEA &amp; VESSELS</h2>
    <div class="photo" role="img" aria-label="Before rosacea treatment, red cheeks and nose" style="left:7px;top:32px;width:103px;height:101px;background:radial-gradient(circle at 50% 40%,#e07f84,var(--rosy) 60%,#efcac6);"></div>
    <div class="photo rounded-end" role="img" aria-label="After rosacea treatment, calmer skin" style="left:114px;top:32px;width:148px;height:101px;background:linear-gradient(160deg,#f3d8d0,#e9c2b8);"></div>
    <p style="top:163px;width:277px;">IPL treatment can reduce rosacea redness and “flushing” to reveal clearer, more natural-looking skin in just a few easy treatments, providing a more permanent result than topical creams. Treatment can reduce rash, redness, flushing, acne-like papules, pustules, and patches, inflammation and broken vessels</p>
  </article>

  <!-- Row two -->
  <article class="treatment" style="left:63px;top:493px;width:280px;">
    <h2>STRETCH MARKS</h2>
    <div class="photo framed" role="img" aria-label="Before stretch mark treatment on the abdomen" style="left:40px;top:26px;width:100px;height:134px;background:linear-gradient(160deg,var(--skin-pale),#d9b5ab);"></div>
    <div class="photo framed" role="img" aria-label="After stretch mark treatment on the abdomen" style="left:138px;top:26px;width:101px;height:134px;background:linear-gradient(160deg,#f1ddd6,#e0c0b6);"></div>
    <p style="top:177px;width:279px;">80% of women and 40% of men have stretch marks. We have the only non-ablative fractional treatment that is FDA approved to minimize the appearance of stretch marks associated with pregnancy, hormonal changes and weight gain. It works by using fractional laser light to break down stretch marks and naturally trigger healthy, new tissue growth, including collagen. Fees are based on the size of the area being treated.</p>
  </article>

  <article class="treatment" style="left:414px;top:493px;width:280px;">
    <h2>TATTOO REMOVAL</h2>
    <div class="photo" role="img" aria-label="Tattoo on a foot before treatment" style="left:0;top:29px;width:91px;height:113px;background:linear-gradient(160deg,#c9a88f,#6f9a58 50%,#b79579);"></div>
    <div class="photo" role="img" aria-label="Faded tattoo after several treatments" style="left:92px;top:29px;width:89px;height:113px;background:linear-gradient(160deg,#b79a88,#8c8478 50%,#c2a392);"></div>
    <div class="photo rounded-end" role="img" aria-label="Skin after tattoo removal" style="left:182px;top:29px;width:89px;height:113px;background:linear-gradient(160deg,#d8bcae,#c7a898);"></div>
    <p style="top:162px;width:277px;">Tattoo regret is experienced by many people, due to employment concerns, relationship status, and overall person growth and life changes. Thankfully, we obtain state of the art laser technology that</p>
  </article>

  <article class="treatment" style="left:767px;top:493px;width:280px;">
    <h2>PIGMENTATION</h2>
    <div class="photo framed" role="img" aria-label="Before pigmentation treatment, freckled skin" style="left:0;top:30px;width:148px;height:68px;background:radial-gradient(circle at 50% 60%,#f0cfc4,#e1a99e);"></div>
    <div class="photo framed" role="img" aria-label="After pigmentation treatment, even skin tone" style="left:127px;top:60px;width:150px;height:68px;background:radial-gradient(circle at 50% 60%,#f6dcd6,#eab9b3);"></div>
    <p style="top:149px;width:277px;">For those of us who’ve spent too much time in the sun, signs of premature aging may be more prominent than we’d like. Laser treatment can clear away skin discoloration and unwanted pigment to reveal more beautiful skin and give you a more revitalized appearance. Commonly called, Photofacials, this treatment treats age spots, sun damage, birthmarks, melasma and freckles. Fees are based on area treated such as spot treatment or full face treatment.</p>
  </article>
</main>
</body>
</html>
```